Statement of Capabilities

We are looking for a fresh new stationary (Word Template) and a new look for our statement of capabilities....logo must be the same.

We are an electrical / lighting contractor-

www.BrightfieldServicing.com

Target Market(s)

B2B and government agencies

Industry/Entity Type

Electrical

Colors
eb1f27
0655a3

Requirements
Must have
• LOGO

```html
<!DOCTYPE html>
<html lang="en">
<head>
<meta charset="utf-8">
<title>Brightfield Servicing – Business Card</title>
<link href="https://fonts.googleapis.com/css2?family=Montserrat:wght@400;600;700;800&display=swap" rel="stylesheet">
<style>
  :root {
    --brand-blue: #1f3a93;
    --brand-red: #e3162b;
    --paper: #f6f7f9;
    --ink: #3a3a3f;
    --backdrop: #e4e4e9;
    --white: #ffffff;
  }
  * { box-sizing: border-box; margin: 0; padding: 0; }
  html, body {
    width: 1200px; height: 934px; overflow: hidden;
    background: var(--backdrop);
    font-family: "Montserrat", Arial, sans-serif;
  }
  .sheet {
    position: relative; width: 1200px; height: 934px;
    display: flex; align-items: center; justify-content: center; gap: 40px;
  }
  .card {
    position: relative; width: 520px; height: 297px; overflow: hidden;
    box-shadow: 0 6px 18px rgba(0,0,0,0.12);
  }

  /* Back of card */
  .card--back { background: var(--brand-blue); color: var(--white); }
  .card--back .wordmark {
    position: absolute; top: 62px; left: 0; right: 0; text-align: center;
  }
  .wordmark__name {
    display: block; font-weight: 800; font-size: 34px; line-height: 1.05;
    letter-spacing: 0.5px; color: var(--brand-red); text-transform: uppercase;
  }
  .wordmark__suffix {
    display: block; font-weight: 800; font-size: 14px; letter-spacing: 1px;
    color: var(--brand-red); text-transform: uppercase; margin-top: 4px;
  }
  .service-list {
    position: absolute; left: 18px; right: 18px; bottom: 40px;
    font-size: 9px; font-weight: 600; letter-spacing: 0.3px; text-transform: uppercase;
  }
  .service-list__row { display: flex; justify-content: center; gap: 4px; white-space: nowrap; }
  .service-list__row--areas { padding-top: 8px; margin-top: 8px; border-top: 1px solid rgba(255,255,255,0.7); }
  .dot { color: var(--brand-red); }

  /* Front of card */
  .card--front { background: var(--paper); }
  .card--front .wordmark { position: absolute; left: 38px; top: 104px; }
  .card--front .wordmark__name { font-size: 30px; text-align: left; }
  .card--front .wordmark__suffix { font-size: 13px; text-align: left; }
  .contact { position: absolute; left: 318px; top: 48px; color: var(--ink); }
  .contact__name { font-size: 17px; font-weight: 700; color: var(--brand-blue); letter-spacing: 0.6px; text-transform: uppercase; }
  .contact__title { font-size: 12px; margin-top: 2px; }
  .contact__lines { list-style: none; margin-top: 18px; font-size: 12px; }
  .contact__lines li { display: flex; align-items: center; gap: 8px; margin-bottom: 4px; }
  .icon { width: 14px; height: 14px; flex: none; }
  .contact__address { margin-top: 14px; font-size: 12px; line-height: 1.7; padding-left: 22px; font-style: normal; }

  .footer-band { position: absolute; left: 0; right: 0; bottom: 18px; height: 10px; background: var(--brand-red); }
  .web-tab {
    position: absolute; left: 28px; bottom: 18px; height: 28px; padding: 0 18px;
    background: var(--brand-blue); color: var(--white); border-radius: 10px 10px 0 0;
    font-size: 12.5px; display: flex; align-items: center; letter-spacing: 0.2px;
  }
</style>
</head>
<body>
<main class="sheet">
  <section class="card card--back" aria-label="Business card back">
    <div class="wordmark">
      <span class="wordmark__name">Brightfield<br>Servicing</span>
      <span class="wordmark__suffix">Incorporated</span>
    </div>
    <div class="service-list">
      <p class="service-list__row">Roadway <span class="dot">•</span> Security <span class="dot">•</span> Commercial <span class="dot">•</span> Sports Lighting <span class="dot">•</span> Electrical <span class="dot">•</span> Washing</p>
      <p class="service-list__row service-list__row--areas">Northern Virginia <span class="dot">•</span> Richmond <span class="dot">•</span> Glenmoor <span class="dot">•</span> Carrollton</p>
    </div>
  </section>

  <section class="card card--front" aria-label="Business card front">
    <div class="wordmark">
      <span class="wordmark__name">Brightfield<br>Servicing</span>
      <span class="wordmark__suffix">Incorporated</span>
    </div>
    <div class="contact">
      <h1 class="contact__name">Jordan Whitley</h1>
      <p class="contact__title">Managing Director</p>
      <ul class="contact__lines">
        <li>
          <svg class="icon" viewBox="0 0 14 14" aria-label="Phone"><rect width="14" height="14" rx="2" fill="#e3162b"/><path d="M4 3.2c.4-.3.9-.2 1.1.2l.8 1.4c.2.4 0 .8-.3 1l-.5.3c.4 1 1.1 1.7 2 2.1l.3-.5c.2-.3.7-.5 1-.3l1.4.8c.4.2.5.7.2 1.1l-.6.7c-.4.4-1 .6-1.6.3C5.9 9.4 4.6 8.1 3.7 6c-.3-.6-.1-1.3.3-1.6z" fill="#fff"/></svg>
          877-555-0142
        </li>
        <li>
          <svg class="icon" viewBox="0 0 14 14" aria-label="Fax"><rect width="14" height="14" rx="2" fill="#e3162b"/><rect x="4.5" y="3" width="5" height="3" fill="#fff"/><rect x="3" y="6" width="8" height="4.5" rx="0.6" fill="#fff"/><rect x="5" y="8.5" width="4" height="2.5" fill="#e3162b"/></svg>
          877-555-0142
        </li>
      </ul>
      <address class="contact__address">415 Harbor Ave Suite B<br>Glenmoor Maryland 21000</address>
    </div>
    <div class="footer-band"></div>
    <div class="web-tab">www.BrightfieldServicing.com</div>
  </section>
</main>
</body>
</html>
```